Solo consultant in research/analytics/data science space needs new business card

I need a new business card to promote my solo business as creative problem solver and consultant. I work on business projects for sales and market research and analytics, customer/market insights, and data science. I provide clients data-informed insights and ideas to enhance their businesses. My initial tagline: 'Make your data work for YOU.'

People should hire me because of my diverse background. Because of my Ph.D. in Political Science I have a strong background in research and analytics, project design and management, and communications skills. With my experience as a marketing analyst, a volunteer on non-profit projects, and currently as research consultant I have worked on projects within various industries. I also have a taste for improvisation so I enjoy thinking creatively and appreciate design thinking.

As an introduction to my background: Clients might want to hire me for many types of projects. Clients might wish to understand who their best customers are and how to characterize them. Maybe clients want to know how their customers feel about a certain product or service. Clients might want to know more about their local market area and overall industry. Clients might want to know whether their marketing programs are effective or else what drives their sales revenue. Perhaps clients want to use their data to create something useful for themselves or their customers.

One client hired me to help them decide whether to expand their services to newer customers. I gathered and analyzed information about the local area – the characteristics of people living there as well as the client’s competitors – and described trends and implications. The client was very pleased with the results and submitted them to superiors for approval to move forward.

For another client – who was looking to purchase a house in a metropolitan area – I gathered population and school data about the area. With this, I created an interactive mapping tool so they could zoom in on neighborhoods and learn more about them before they selected a neighborhood to purchase a house. They were happy with the results of my work.

When I worked as a marketing analyst for a consulting firm, a Vice President of Marketing hired us to discover whether or not the company’s marketing programs (i.e. coupons and discounts) were effective. I analyzed their data and our team discovered their marketing was indeed effective. He was very happy and used this to justify their programs to the Finance department (who thought such programs lost revenue).

- Marcus Delano Whitby, Ph.D.

Target Market(s)

Future clients and employers. The most immediate target markets will be other service providers such as consulting companies, marketing firms and ad agencies. I will also use this for meeting with clients in various industries.

Industry/Entity Type

Consulting

Contact Information for Business Card

Since it is my first real business card as a solo practitioner, I want to make an excellent first impression. I want this useful in case someone hires me to work on projects or else hire me to work within a firm or company. The card should convey competence and some creativity while also being neither stuffy nor a data geek.

Colors

Designer to choose colors to be used in the design.

Requirements
Nice to have
• Attached are the starting efforts at the card to add some color. It will be nice to use my name and descriptors on one side and tagline on the other. If anyone has better ideas, I will love to see them!

```html
<!DOCTYPE html>
<html lang="en">
<head>
<meta charset="utf-8">
<title>Marcus Delano Whitby, Ph.D — Business Card</title>
<link rel="stylesheet" href="https://fonts.googleapis.com/css2?family=Roboto:wght@400;500;700&display=swap">
<style>
  :root {
    --coral: #e05e4b;
    --charcoal: #2e2e2e;
    --ink: #3a3a3a;
    --muted: #555555;
    --paper: #ffffff;
    --backdrop: #dedede;
  }
  * { margin: 0; padding: 0; box-sizing: border-box; }
  html, body {
    width: 1125px;
    height: 1200px;
    overflow: hidden;
    background: var(--backdrop);
    font-family: "Roboto", sans-serif;
  }
  .canvas { position: relative; width: 1125px; height: 1200px; }

  .card {
    position: absolute;
    left: 171px;
    width: 826px;
    height: 472px;
  }
  .card--front { top: 106px; background: var(--paper); }
  .card--back  { top: 639px; background: var(--coral); }

  .centered { position: absolute; left: 0; right: 0; text-align: center; white-space: nowrap; }

  .name {
    top: 110px;
    font-size: 45px;
    font-weight: 500;
    color: var(--coral);
    line-height: 1;
  }
  .specialties {
    top: 167px;
    font-size: 20.5px;
    font-weight: 500;
    color: var(--ink);
    line-height: 1;
  }
  .role {
    top: 219px;
    font-size: 31px;
    font-weight: 400;
    color: var(--coral);
    line-height: 1;
  }
  .location {
    top: 256px;
    font-size: 19px;
    color: var(--muted);
    line-height: 1;
  }
  .contact-row {
    display: flex;
    justify-content: center;
    align-items: center;
    gap: 10px;
    font-size: 19.5px;
    color: var(--muted);
    line-height: 1;
  }
  .contact-row--primary { top: 306px; }
  .contact-row--secondary { top: 333px; gap: 4px; }
  .contact-item { display: inline-flex; align-items: center; gap: 3px; }
  .contact-icon { width: 18px; height: 18px; flex: none; }

  .card-band {
    position: absolute;
    left: 0;
    bottom: 0;
    width: 826px;
    height: 21px;
  }

  .tagline {
    top: 170px;
    font-size: 53px;
    font-weight: 700;
    color: var(--charcoal);
    line-height: 64px;
  }
</style>
</head>
<body>
<main class="canvas">

  <section class="card card--front" aria-label="Card front">
    <h1 class="centered name">Marcus Delano Whitby, Ph.D</h1>
    <p class="centered specialties">Research/Analytics-Customer Intelligence - Data Science</p>
    <h2 class="centered role">Consultant</h2>
    <p class="centered location">Lisbon,PT</p>

    <div class="centered contact-row contact-row--primary">
      <span class="contact-item">
        <svg class="contact-icon" viewBox="0 0 24 24" aria-hidden="true">
          <path fill="#e05e4b" d="M6.6 10.8c1.4 2.8 3.8 5.1 6.6 6.6l2.2-2.2c.3-.3.7-.4 1-.2 1.1.4 2.3.6 3.6.6.6 0 1 .4 1 1V20c0 .6-.4 1-1 1C10.6 21 3 13.4 3 4c0-.6.4-1 1-1h3.5c.6 0 1 .4 1 1 0 1.3.2 2.5.6 3.6.1.3 0 .7-.2 1L6.6 10.8z"/>
        </svg>
        +351 912 305 648
      </span>
      <span class="contact-item">
        <svg class="contact-icon" viewBox="0 0 24 24" aria-hidden="true">
          <rect x="2" y="5" width="20" height="14" rx="1.5" fill="#e05e4b"/>
          <path d="M3 6.5l9 6 9-6" fill="none" stroke="#ffffff" stroke-width="1.8"/>
        </svg>
        mdwhitby70@inboxmail.com
      </span>
    </div>

    <div class="centered contact-row contact-row--secondary">
      <span class="contact-item">
        <svg class="contact-icon" viewBox="0 0 24 24" aria-hidden="true">
          <circle cx="12" cy="12" r="9.5" fill="#e05e4b"/>
          <ellipse cx="12" cy="12" rx="4" ry="9.5" fill="none" stroke="#ffffff" stroke-width="1.4"/>
          <path d="M2.5 12h19M4 7.5h16M4 16.5h16" stroke="#ffffff" stroke-width="1.2"/>
        </svg>
        marcuswhitby.com
      </span>
      <span class="contact-item">
        <svg class="contact-icon" viewBox="0 0 24 24" aria-hidden="true">
          <circle cx="12" cy="12" r="8" fill="#e05e4b"/>
        </svg>
        @MarcusWhitby70
      </span>
    </div>

    <svg class="card-band" viewBox="0 0 826 21" preserveAspectRatio="none" aria-hidden="true">
      <polygon points="0,0 535,0 528,21 0,21" fill="#e05e4b"/>
      <polygon points="541,0 826,0 826,21 534,21" fill="#2e2e2e"/>
    </svg>
  </section>

  <section class="card card--back" aria-label="Card back">
    <p class="centered tagline">Make your data<br>work for you.</p>
  </section>

</main>
</body>
</html>
```